Chewing Gum With Active Ingredients Needs Packaging Design

Brivella Mint Systems is a revolutionary new chewing gum that contains active ingredients commonly found in mouthwashes - it's a portable and convenient way to keep a fresh, clean, and healthy mouth. We have a thorough design brief (attached file) for the packaging we need - a simple sleeve for blister packed gum. We want our design to convey that we are a modern, effective, and high-end product.

Target Market(s)

Young professionals, 20-35 years old

Font styles to use
Serif
Sans Serif

Colors
0292cd
ffffff
0555a3

Requirements
Must have
• A sleek, elegant design
• ALL of the elements listed in the creative brief PDF
• Attached logo
Nice to have
• Incorporation of foil into the design
• A unique, unmistakable look
Should not have
• Too medical of a look

```html
<!DOCTYPE html>
<html lang="en">
<head>
<meta charset="utf-8">
<title>Brivella Mint Systems – Gum Sleeve</title>
<link rel="stylesheet" href="https://fonts.googleapis.com/css2?family=Montserrat:wght@300;400;700&display=swap">
<style>
  :root {
    --navy: #2b2a86;
    --blue-mid: #0555a3;
    --blue-bright: #0292cd;
    --white: #ffffff;
    --canvas: #eef1f5;
    --facet-light: #f3f4f6;
    --facet-mid: #e3e6ea;
    --gum-green: #9fc3a6;
    --foil-grey: #8d8f91;
  }
  * { margin: 0; padding: 0; box-sizing: border-box; }
  html, body {
    width: 1200px; height: 1200px; overflow: hidden;
    background: var(--canvas);
    font-family: "Montserrat", sans-serif;
  }
  .sleeve {
    position: absolute; left: 100px; top: 330px;
    width: 1000px; height: 540px;
    background: var(--white);
    overflow: hidden;
  }
  .sleeve__top-band {
    position: absolute; left: 0; top: 0; width: 100%; height: 27px;
    background: linear-gradient(90deg, var(--navy), var(--blue-mid) 55%, var(--blue-bright));
  }
  .sleeve__facets {
    position: absolute; left: 0; top: 27px; width: 100%; height: 360px;
    background: linear-gradient(160deg, var(--facet-light) 0%, var(--white) 35%, var(--facet-mid) 60%, var(--white) 100%);
    opacity: 0.8;
  }
  .brand {
    position: absolute; left: 0; top: 44px; width: 975px;
    text-align: center; color: var(--navy);
    font-weight: 300;
  }
  .brand__mark {
    width: 82px; height: 82px; margin: 0 auto 14px;
    border-radius: 50%; border: 4px solid var(--navy);
  }
  .brand__name {
    font-size: 38px; letter-spacing: 2px; line-height: 1;
  }
  .brand__tagline {
    font-size: 10px; letter-spacing: 14px; margin-top: 6px;
  }
  .claims {
    position: absolute; right: 48px; top: 50px;
    font-size: 12px; line-height: 1.15; text-align: center;
    color: var(--navy);
  }
  .window {
    position: absolute; left: 925px; top: 183px;
    width: 80px; height: 159px;
    border: 5px solid var(--blue-bright); border-right: none;
    border-bottom-color: var(--navy);
    border-left-color: var(--blue-mid);
    border-radius: 14px 0 0 14px;
    background: linear-gradient(180deg, var(--gum-green), var(--foil-grey) 50%, var(--gum-green));
  }
  .count {
    position: absolute; left: 22px; top: 445px;
    font-size: 15px; line-height: 1; color: var(--navy); text-align: center;
  }
  .count__number { font-weight: 700; }
  .flavour {
    position: absolute; right: 18px; top: 461px;
    font-size: 15px; font-weight: 700; color: var(--navy);
  }
  .benefits {
    position: absolute; left: 0; bottom: 0; width: 100%; height: 47px;
    background: linear-gradient(90deg, var(--navy), var(--blue-mid) 45%, var(--blue-bright));
    color: var(--white); font-size: 15px; font-weight: 300;
    display: flex; align-items: center; justify-content: center; gap: 12px;
    padding-right: 40px;
  }
  .benefits__dot { font-size: 10px; }
</style>
</head>
<body>
  <section class="sleeve">
    <div class="sleeve__top-band"></div>
    <div class="sleeve__facets" role="img" aria-label="Faint white and pale grey faceted triangle pattern"></div>

    <div class="brand">
      <div class="brand__mark"></div>
      <div class="brand__name">BRIVELLA</div>
      <div class="brand__tagline">MINT SYSTEMS</div>
    </div>

    <div class="claims">ASPARTAME FREE<br>WITH XYLITOL</div>

    <div class="window" role="img" aria-label="Window showing green gum pieces in the foil blister"></div>

    <div class="count">
      <div class="count__number">8 PIECES</div>
      <div>SUGAR FREE GUM</div>
    </div>

    <div class="flavour">PEPPERMINT</div>

    <div class="benefits">
      <span>WHITENS TEETH</span><span class="benefits__dot">•</span>
      <span>FRESHENS BREATH</span><span class="benefits__dot">•</span>
      <span>HELPS REDUCE PLAQUE</span><span class="benefits__dot">•</span>
      <span>HELPS PROTECT GUMS</span>
    </div>
  </section>
</body>
</html>
```